Need to design a business card with logo

Hellow
we are a company ,
PT KORAN MELATI JAYA
looking for design of name card.
what we do is property development and management.
design preferable professional corporate look and feel.
corporate. color, pantone colour 289
information required is
company name " Koran Melati Jaya"
person name eg " Peter Walsh"
person title eg "secret agent"
address: 12 heron lane , jakarta, indonesia
phone : +6221 5917264
mobile : 0812 463 518
email : peter@walshmail.example
website: www.peterwa.example
if you want to include logo in the design you are welcome and appreciated , or you can simply use the company name as the logo.
thanks
Target Market(s)
corporate , business person , show events, exhibition events ,etc
Industry/Entity Type
Business
Look and feel
Each slider illustrates characteristics of the customer's brand and the style your logo design should communicate.

```html
<!DOCTYPE html>
<html lang="en">
<head>
<meta charset="utf-8">
<title>Koran Melati Jaya – Business Cards</title>
<link href="https://fonts.googleapis.com/css2?family=Arimo:wght@400;700&family=Fjalla+One&display=swap" rel="stylesheet">
<style>
  :root{
    --backdrop:#3a3a3a;
    --navy:#0f2a5c;
    --navy-deep:#0b2150;
    --navy-band:#0c2556;
    --brand-blue:#1a8fd0;
    --ink:#3a3a3a;
    --white:#ffffff;
    --silver:#b9bcc2;
    --link:#1a9ad6;
    --rule:#5a5a5a;
  }
  *{box-sizing:border-box;margin:0;padding:0}
  html,body{width:1200px;height:900px;overflow:hidden}
  body{background:var(--backdrop);position:relative;font-family:"Arimo",Arial,sans-serif}
  .card{position:absolute;width:514px;height:292px;border-radius:28px;overflow:hidden}
  .card--front{background:linear-gradient(160deg,#143468 0%,var(--navy) 55%,var(--navy-deep) 100%)}
  .card--back{background:var(--white)}
  .pos-a{left:70px;top:158px}
  .pos-b{left:606px;top:158px}
  .pos-c{left:70px;top:472px}
  .pos-d{left:606px;top:472px}

  .brand-mark{position:absolute;border-radius:50%}
  .brand-name{position:absolute;font-weight:700;white-space:nowrap;letter-spacing:-0.2px}
  .brand-tagline{position:absolute;white-space:nowrap}

  /* front, centred */
  .pos-a .brand-mark{left:208px;top:52px;width:116px;height:116px;background:var(--white)}
  .pos-a .brand-name{left:0;width:100%;text-align:center;top:184px;font-size:23px;color:var(--white)}
  .pos-a .brand-tagline{left:0;width:100%;text-align:center;top:209px;font-size:11px;color:var(--white)}

  /* front, with stripe field */
  .stripe-field{position:absolute;left:0;top:0;width:250px;height:292px;
    background:linear-gradient(100deg,#c4c6cb 0%,#6f93c0 30%,#1f7cc0 55%,rgba(15,42,92,0) 100%)}
  .pos-c{background:var(--navy-deep)}
  .pos-c .brand-mark{left:254px;top:223px;width:50px;height:50px;background:var(--silver)}
  .pos-c .brand-name{left:312px;top:236px;font-size:18px;color:var(--silver)}
  .pos-c .brand-tagline{left:313px;top:256px;font-size:9px;color:var(--silver)}

  /* backs */
  .back-brand .brand-mark{left:100px;top:97px;width:70px;height:70px;background:linear-gradient(180deg,var(--brand-blue),var(--navy))}
  .back-brand .brand-name{left:50px;width:170px;text-align:center;top:176px;font-size:17px;color:var(--brand-blue)}
  .divider{position:absolute;left:245px;top:64px;width:1.5px;height:162px;background:var(--rule)}
  .holder{position:absolute;left:274px;top:66px}
  .holder-name{font-family:"Fjalla One","Oswald",sans-serif;font-size:25px;color:var(--navy);line-height:1;letter-spacing:0.3px}
  .holder-title{font-size:13px;color:var(--ink);margin-top:3px}
  .contacts{list-style:none;margin-top:17px}
  .contacts li{font-size:13px;color:var(--ink);line-height:14.5px;display:flex;align-items:center;gap:6px}
  .contacts li.web{color:var(--link)}
  .contacts svg{width:9px;height:9px;flex:none}
  .address{font-size:13px;color:var(--ink);line-height:14.5px;margin-top:14px}

  .foot-line{position:absolute;left:0;width:100%;top:268px;height:4px;background:var(--brand-blue)}
  .foot-band{position:absolute;left:0;width:100%;top:276px;height:16px;background:var(--navy-band)}
</style>
</head>
<body>

<section class="card card--front pos-a">
  <span class="brand-mark"></span>
  <span class="brand-name">KORAN MELATI JAYA</span>
  <span class="brand-tagline">property development and management</span>
</section>

<section class="card card--front pos-c">
  <div class="stripe-field" role="img" aria-label="Diagonal stripe pattern in silver and blue"></div>
  <span class="brand-mark"></span>
  <span class="brand-name">KORAN MELATI JAYA</span>
  <span class="brand-tagline">property development and management</span>
</section>

<section class="card card--back pos-b">
  <div class="back-brand">
    <span class="brand-mark"></span>
    <span class="brand-name">KORAN MELATI JAYA</span>
  </div>
  <span class="divider"></span>
  <div class="holder">
    <h1 class="holder-name">PETER WALSH</h1>
    <p class="holder-title">General Manager</p>
    <ul class="contacts">
      <li><svg viewBox="0 0 10 10"><rect x="1" y="0" width="8" height="10" rx="1" fill="#0f2a5c"/><rect x="3" y="2" width="4" height="2" fill="#fff"/></svg>+6221 5917264</li>
      <li><svg viewBox="0 0 10 10"><rect x="1" y="0" width="8" height="10" rx="1" fill="#0f2a5c"/><rect x="3" y="2" width="4" height="5" fill="#fff"/></svg>0812 463 518</li>
      <li><svg viewBox="0 0 10 10"><rect x="0" y="2" width="10" height="7" fill="#0f2a5c"/><path d="M0 2 L5 6 L10 2" stroke="#fff" fill="none"/></svg>peter@walshmail.example</li>
      <li class="web"><svg viewBox="0 0 10 10"><rect width="10" height="10" fill="#0f2a5c"/><path d="M3 2 L3 8 L5 6 L7 8" stroke="#fff" fill="none"/></svg>www.peterwa.example</li>
    </ul>
    <p class="address">12 heron lane<br>Jakarta, Indonesia</p>
  </div>
</section>

<section class="card card--back pos-d">
  <div class="back-brand">
    <span class="brand-mark"></span>
    <span class="brand-name">KORAN MELATI JAYA</span>
  </div>
  <span class="divider"></span>
  <div class="holder">
    <h1 class="holder-name">PETER WALSH</h1>
    <p class="holder-title">General Manager</p>
    <ul class="contacts">
      <li><svg viewBox="0 0 10 10"><rect x="1" y="0" width="8" height="10" rx="1" fill="#0f2a5c"/><rect x="3" y="2" width="4" height="2" fill="#fff"/></svg>+6221 5917264</li>
      <li><svg viewBox="0 0 10 10"><rect x="1" y="0" width="8" height="10" rx="1" fill="#0f2a5c"/><rect x="3" y="2" width="4" height="5" fill="#fff"/></svg>0812 463 518</li>
      <li><svg viewBox="0 0 10 10"><rect x="0" y="2" width="10" height="7" fill="#0f2a5c"/><path d="M0 2 L5 6 L10 2" stroke="#fff" fill="none"/></svg>peter@walshmail.example</li>
      <li class="web"><svg viewBox="0 0 10 10"><rect width="10" height="10" fill="#0f2a5c"/><path d="M3 2 L3 8 L5 6 L7 8" stroke="#fff" fill="none"/></svg>www.peterwa.example</li>
    </ul>
    <p class="address">12 heron lane<br>Jakarta, Indonesia</p>
  </div>
  <span class="foot-line"></span>
  <span class="foot-band"></span>
</section>

</body>
</html>
```